依頼詳細
作りたいチラシのイメージは、「参考画像.jpg」の通りです。

裏面のデザイン(価格表)は完成しておりますので、デザインの雰囲気をなるべく合わせていただけると幸いです。(「裏面画像.jpg」)
また、以前に表面のデザインも作成しておりますので、こちらも参考にしてください。(「表面画像.jpg」)

特に、
・往診料無料
・ワクチン料金
・フィラリア症予防薬料金
・自宅で手軽に予防ができる
上記の内容をより訴求できるデザインにしたいと思っております。

動物病院ですので、優しく、特に女性受けが良さそうなイメージで作成をお願いいたします。

使用する色は、主に「緑、オレンジ」をメインに考えておりますが、色の具合は自由に調節いただいて結構です。
作りたいチラシのイメージは、「参考画像.jpg」の通りですが、デザインは自由に調節していただいて結構です。
また、こちらで用意させていただく素材以外で、デザインに沿った文言・イラスト・アイコン・写真などがありましたら、自由に取り入れていただければと思います。
記載項目
・チラシに使用する文章はこちらで用意いたします。

「参考画像.jpg」の①~⑩にはPDFファイル(チラシ記載内容.pdf)に記載されている文章を使用してください。

・院長の画像については、画像1、画像2のいずれかをお使いください。
※psd形式以外のデータをご希望の際はお申し付けください。

・ロゴについては画像3をお使いください。
サイズ
A4
ページ数
片面
希望イメージ
• +5 0 +5
• シンプル
複雑
• 単色
カラフル
• 暗い
明るい
• 日常
高級
• 遊び心
厳粛
• 未来的
伝統的
• 女性的
男性的
希望する色
納品ファイル
• 高解像度JPG (.jpg)
• イラストレーター形式 (.ai)
補足説明
依頼公開後の追記内容
■ 選んだ理由

全体的なイメージと、特に家のデザインが気に入りました。

■ 提案者全員のお礼・コメント

この度はご提案くださり誠にありがとうございました。
どれも良いものばかりで、選択に非常に迷いました。

また機会がございましたら、その時はどうぞよろしくお願いいたします。

```html
<!DOCTYPE html>
<html lang="ja">
<head>
<meta charset="UTF-8">
<title>ひだまり動物病院 往診チラシ</title>
<link rel="stylesheet" href="https://fonts.googleapis.com/css2?family=M+PLUS+Rounded+1c:wght@400;700;800;900&family=Noto+Sans+JP:wght@400;500;700&display=swap">
<style>
:root{
  --green:#5db52f;
  --green-dark:#3f8d1c;
  --green-pale:#edf6e1;
  --green-line:#b9dc9c;
  --orange:#f08300;
  --orange-pale:#fff4d8;
  --pink:#f2a2b6;
  --ink:#3b3b3b;
  --white:#ffffff;
}
*{margin:0;padding:0;box-sizing:border-box}
html,body{width:846px;height:1200px;overflow:hidden;background:var(--white)}
body{font-family:"Noto Sans JP",sans-serif;color:var(--ink)}
.flyer{position:relative;width:846px;height:1200px;background:var(--white);overflow:hidden}

/* header */
.call-bubble{position:absolute;left:16px;top:22px;width:120px;height:94px;background:var(--orange);color:var(--white);
  border-radius:50%;display:flex;align-items:center;justify-content:center;text-align:center;
  font-family:"M PLUS Rounded 1c",sans-serif;font-weight:800;font-size:17px;line-height:1.3;z-index:2}
.call-bubble::after{content:"";position:absolute;right:6px;bottom:4px;border:10px solid transparent;border-top-color:var(--orange);transform:rotate(-35deg)}
.director-photo{position:absolute;left:28px;top:60px;width:210px;height:250px;
  background:linear-gradient(180deg,#eef3f3 0%,#c9d7dc 60%,#4d6f86 100%);border-radius:6px}
.director-name{position:absolute;left:60px;top:280px;font-size:12px;color:var(--ink);z-index:2}

.hero{position:absolute;left:252px;top:0;width:580px;height:190px}
.hero-house{position:absolute;left:0;top:0}
.hero-lead{position:absolute;left:70px;top:18px;background:var(--green);color:var(--white);
  font-family:"M PLUS Rounded 1c",sans-serif;font-weight:900;font-size:40px;padding:0 16px;border-radius:8px;line-height:56px}
.hero-main{position:absolute;left:30px;top:78px;font-family:"M PLUS Rounded 1c",sans-serif;font-weight:900;
  color:var(--green);font-size:70px;line-height:1}
.hero-sub{position:absolute;left:60px;top:152px;font-family:"M PLUS Rounded 1c",sans-serif;font-weight:900;
  color:var(--green);font-size:44px;line-height:1.1}
.pets-art{position:absolute;right:0;top:10px;width:150px;height:70px;border-radius:30px;
  background:linear-gradient(90deg,#f5a34a 0%,#f7c590 55%,#f4b3c2 100%)}

.feature-pill{position:absolute;right:16px;width:262px;height:40px;background:var(--green);color:var(--white);
  border-radius:6px;font-family:"M PLUS Rounded 1c",sans-serif;font-weight:800;font-size:22px;
  display:flex;align-items:center;justify-content:center}
.pill-vaccine{top:190px}
.pill-filaria{top:238px}

.free-banner{position:absolute;left:246px;top:296px;width:584px;height:54px;background:var(--orange-pale);
  border-bottom:4px solid var(--orange);border-radius:6px 6px 0 0;display:flex;align-items:center;padding-left:22px;
  font-family:"M PLUS Rounded 1c",sans-serif;font-weight:900;color:var(--orange)}
.free-banner strong{font-size:38px}
.free-banner span{font-size:24px;margin-left:4px}

/* price section */
.price-area{position:absolute;left:0;top:360px;width:846px;height:330px;background:var(--green-pale)}
.price-card{position:absolute;top:18px;background:var(--white);border:2px solid var(--green);border-radius:10px;overflow:hidden}
.vaccine-card{left:30px;width:380px;height:260px}
.filaria-card{left:424px;width:392px;height:260px}
.card-title{height:40px;background:var(--green);color:var(--white);font-family:"M PLUS Rounded 1c",sans-serif;
  font-weight:800;font-size:22px;display:flex;align-items:center;justify-content:center}
table{border-collapse:collapse;width:100%}
.price-table td,.price-table th{border-bottom:1px dashed var(--green-line);height:35px;font-size:16px}
.price-table .kind{width:34px;background:var(--orange);color:var(--white);font-weight:700;font-size:14px;text-align:center;
  writing-mode:vertical-rl;border-bottom:2px solid var(--white)}
.price-table .kind.cat{background:var(--pink)}
.price-table .item{padding-left:14px}
.price-table .yen{text-align:right;padding-right:20px;font-weight:700;color:var(--ink)}
.price-table .yen b{color:var(--orange);font-size:18px}
.filaria-table th{font-size:11px;font-weight:500;height:22px;color:var(--green-dark)}
.filaria-table td{height:32px}
.filaria-table .weight{padding-left:12px;font-size:15px}
.filaria-table .yen{padding-right:16px}
.filaria-table .yen.year b{color:var(--orange)}
.filaria-table .yen.once b{color:var(--ink)}
.price-note{position:absolute;left:32px;top:292px;font-size:12px;color:var(--ink)}

/* schedule */
.schedule{position:absolute;left:30px;top:704px;width:786px}
.schedule-head{display:flex;gap:8px}
.schedule-head div{background:var(--green);color:var(--white);font-family:"M PLUS Rounded 1c",sans-serif;font-weight:800;
  font-size:18px;height:34px;display:flex;align-items:center;justify-content:center;border-radius:6px 6px 0 0}
.head-date{width:390px}
.head-area{width:388px}
.schedule-table td{border:1px solid var(--green-line);font-size:11px;line-height:1.5;vertical-align:middle;padding:4px 8px}
.schedule-table .pref{width:70px;background:var(--green-pale);color:var(--green-dark);font-weight:700;font-size:13px;text-align:center}
.schedule-table .dates{width:320px}
.schedule-table tr{height:42px}
.schedule-note{position:absolute;left:30px;top:958px;font-size:11px}

/* contact */
.contact{position:absolute;left:30px;top:982px;width:786px;height:206px;border:3px solid var(--green);border-radius:12px;overflow:hidden;background:var(--white)}
.contact-head{height:34px;background:var(--green);color:var(--white);font-family:"M PLUS Rounded 1c",sans-serif;font-weight:800;
  font-size:20px;display:flex;align-items:center;justify-content:center}
.phone-line{position:absolute;left:200px;top:42px;display:flex;align-items:center;gap:10px;color:var(--green-dark)}
.phone-line strong{font-family:"M PLUS Rounded 1c",sans-serif;font-weight:900;font-size:46px;letter-spacing:1px;line-height:60px}
.mail-line{position:absolute;left:250px;top:104px;font-family:"M PLUS Rounded 1c",sans-serif;font-weight:700;font-size:20px;color:var(--green-dark)}
.clinic-id{position:absolute;left:200px;top:140px;display:flex;align-items:center;gap:10px}
.clinic-mark{width:22px;height:22px;border-radius:50%;background:var(--green)}
.clinic-name{font-family:"M PLUS Rounded 1c",sans-serif;font-weight:800;font-size:26px;color:var(--green-dark)}
.clinic-address{font-size:11px;line-height:1.4;margin-left:10px}
.pets-bottom{position:absolute;left:10px;top:48px;width:170px;height:140px;border-radius:14px;
  background:linear-gradient(90deg,#f7c590,#fbe2c4)}
.hours{position:absolute;right:14px;top:58px;width:116px;height:116px;border-radius:50%;background:var(--orange);color:var(--white);
  display:flex;flex-direction:column;align-items:center;justify-content:center;font-family:"M PLUS Rounded 1c",sans-serif;font-weight:800}
.hours span{font-size:18px}
.hours strong{font-size:18px;margin-top:4px}
</style>
</head>
<body>
<div class="flyer">

  <header>
    <div class="call-bubble">お気軽に<br>ご連絡<br>ください！</div>
    <div class="director-photo" role="img" aria-label="聴診器をかけた院長の写真"></div>
    <p class="director-name">院長：森田 悠</p>

    <div class="hero">
      <svg class="hero-house" width="440" height="190" viewBox="0 0 440 190" aria-hidden="true">
        <path d="M20 70 L220 6 L420 70" fill="none" stroke="#5db52f" stroke-width="6" stroke-linecap="round" stroke-linejoin="round"/>
      </svg>
      <div class="hero-lead">ワクチンは</div>
      <div class="hero-main">おウチで</div>
      <div class="hero-sub">が新しい！</div>
      <div class="pets-art" role="img" aria-label="犬と猫のシルエットのイラスト"></div>
    </div>

    <div class="feature-pill pill-vaccine">自宅でワクチン</div>
    <div class="feature-pill pill-filaria">自宅でフィラリア予防</div>

    <div class="free-banner"><strong>往診料無料</strong><span>でお伺いします！</span></div>
  </header>

  <section class="price-area">
    <div class="price-card vaccine-card">
      <div class="card-title">ワクチン料金表</div>
      <table class="price-table">
        <tr><td class="kind" rowspan="4">犬用</td><td class="item">狂犬病ワクチン</td><td class="yen"><b>2,500</b>円</td></tr>
        <tr><td class="item">9種混合ワクチン</td><td class="yen"><b>5,000</b>円</td></tr>
        <tr><td class="item">8種混合ワクチン</td><td class="yen"><b>4,800</b>円</td></tr>
        <tr><td class="item">6種混合ワクチン</td><td class="yen"><b>4,000</b>円</td></tr>
        <tr><td class="kind cat" rowspan="2">猫用</td><td class="item">3種混合ワクチン</td><td class="yen"><b>4,000</b>円</td></tr>
        <tr><td class="item">5種混合ワクチン</td><td class="yen"><b>5,000</b>円</td></tr>
      </table>
    </div>

    <div class="price-card filaria-card">
      <div class="card-title">フィラリア症予防薬 料金表</div>
      <table class="price-table filaria-table">
        <tr><th></th><th>1回分</th><th>1回分×6ヵ月分</th></tr>
        <tr><td class="weight">5kg未満</td><td class="yen once"><b>600</b>円</td><td class="yen year"><b>4,200</b>円</td></tr>
        <tr><td class="weight">5kg〜10kg</td><td class="yen once"><b>700</b>円</td><td class="yen year"><b>4,800</b>円</td></tr>
        <tr><td class="weight">10kg〜20kg</td><td class="yen once"><b>900</b>円</td><td class="yen year"><b>6,300</b>円</td></tr>
        <tr><td class="weight">20kg〜30kg</td><td class="yen once"><b>1,100</b>円</td><td class="yen year"><b>7,700</b>円</td></tr>
        <tr><td class="weight">30kg〜40kg</td><td class="yen once"><b>1,300</b>円</td><td class="yen year"><b>9,100</b>円</td></tr>
        <tr><td class="weight">40kg以上</td><td class="yen once"><b>1,500</b>円</td><td class="yen year"><b>10,500</b>円</td></tr>
      </table>
    </div>
    <p class="price-note">※他の料金についてはお問い合わせください。</p>
  </section>

  <section class="schedule">
    <div class="schedule-head"><div class="head-date">往診スケジュール</div><div class="head-area">往診対応地域</div></div>
    <table class="schedule-table">
      <tr><td class="pref">栃木県</td><td class="dates">4/10(月)・4/24(月)・5/8(月)・5/22(月)・6/5(月)</td><td>みどり市 / 若葉町 / 緑ヶ丘 / 北台 / 南台 ほか近隣地域</td></tr>
      <tr><td class="pref">群馬県</td><td class="dates">4/12(水)・4/26(水)・5/10(水)・5/24(水)</td><td>東町 / 西町 / 中央 / 本町 ほか</td></tr>
      <tr><td class="pref">埼玉県</td><td class="dates">4/14(金)・4/28(金)・5/12(金)・5/26(金)</td><td>全域</td></tr>
      <tr><td class="pref">東京都</td><td class="dates">4/15(土)・4/29(土)・5/13(土)・5/27(土)</td><td>全域</td></tr>
      <tr><td class="pref">神奈川県</td><td class="dates">4/16(日)・4/30(日)・5/14(日)・5/28(日)</td><td>港北 / 青葉 / 都筑 / 中原 ほか近隣地域</td></tr>
    </table>
  </section>
  <p class="schedule-note">※上記以外の日程・地域でも往診可能です。詳しくはお問い合わせください。</p>

  <footer class="contact">
    <div class="contact-head">往診のご予約・ご相談はこちら</div>
    <div class="pets-bottom" role="img" aria-label="寄り添う犬と猫のイラスト"></div>
    <div class="phone-line">
      <svg width="40" height="40" viewBox="0 0 24 24" aria-hidden="true"><path fill="#3f8d1c" d="M6.6 10.8a15.1 15.1 0 0 0 6.6 6.6l2.2-2.2a1 1 0 0 1 1-.25 11.4 11.4 0 0 0 3.6.57 1 1 0 0 1 1 1V20a1 1 0 0 1-1 1A17 17 0 0 1 3 4a1 1 0 0 1 1-1h3.5a1 1 0 0 1 1 1c0 1.25.2 2.450.57 3.57a1 1 0 0 1-.25 1z"/></svg>
      <strong>080-1234-5678</strong>
    </div>
    <p class="mail-line">メール：info@hidamari-vet.example</p>
    <div class="clinic-id">
      <span class="clinic-mark"></span>
      <span class="clinic-name">ひだまり動物病院</span>
      <span class="clinic-address">〒320-0000<br>栃木県みどり市若葉町1-2-3<br>TEL 0284-00-1234</span>
    </div>
    <div class="hours"><span>受付時間</span><strong>9:00〜21:00</strong></div>
  </footer>

</div>
</body>
</html>
```